Plovenworks business card

We need a modern business card - With our 4 colors - See web: www.plovenworks.dk

I have attached logo and som old business Cards we have - Lets Make the new ones shine...:-) -

Industry/Entity Type

Business

Requirements
Must have
• the logo with plovnworks only,

```html
<!DOCTYPE html>
<html lang="da">
<head>
<meta charset="utf-8">
<title>Plovenworks – visitkort</title>
<link rel="stylesheet" href="https://fonts.googleapis.com/css2?family=Arimo:wght@400;700&display=swap">
<style>
  :root {
    --backdrop: #3a3a3c;
    --card-dark: #231f20;
    --card-light: #ffffff;
    --brand-green: #8dc63f;
    --text-grey: #6d6e71;
    --text-dark: #414042;
    --text-white: #ffffff;
  }
  * { box-sizing: border-box; margin: 0; padding: 0; }
  html, body {
    width: 1200px; height: 950px; overflow: hidden;
    background: var(--backdrop);
    font-family: "Arimo", Arial, sans-serif;
  }
  .sheet {
    width: 1200px; height: 950px;
    display: flex; flex-direction: column;
    align-items: center; justify-content: center; gap: 36px;
  }
  .card {
    position: relative;
    width: 650px; height: 420px;
    overflow: hidden;
    box-shadow: 0 8px 24px rgba(0,0,0,.35);
  }

  /* Back side */
  .card--back { background: var(--card-dark); }
  .card--back .brand {
    position: absolute; right: 70px; bottom: 90px;
    display: flex; align-items: center; gap: 12px;
    color: var(--text-white);
  }
  .brand__dot {
    width: 18px; height: 18px; border-radius: 50%;
    background: currentColor;
  }
  .brand__name { font-size: 28px; font-weight: 400; letter-spacing: 2px; }

  /* Front side */
  .card--front { background: var(--card-light); }
  .name-band {
    position: absolute; left: 200px; right: 0; top: 34px; height: 110px;
    background: var(--brand-green);
    color: var(--text-white);
    padding: 26px 0 0 170px;
  }
  .name-band__name { font-size: 25px; font-weight: 700; }
  .name-band__title { font-size: 17px; margin-top: 6px; padding-left: 12px; }

  .identity {
    position: absolute; left: 60px; top: 150px; width: 190px;
    color: var(--text-dark);
  }
  .identity .brand { display: flex; align-items: center; gap: 10px; color: var(--brand-green); }
  .identity .brand__dot { width: 14px; height: 14px; }
  .identity .brand__name { font-size: 22px; letter-spacing: 1.5px; }
  .identity__rule {
    height: 2px; background: var(--brand-green);
    margin: 12px 0 8px; width: 170px;
  }
  .identity__tagline { font-size: 12px; text-align: center; width: 170px; color: var(--text-dark); }

  .contact {
    position: absolute; left: 400px; top: 190px;
    list-style: none; color: var(--text-grey); font-size: 16px;
  }
  .contact li { display: flex; align-items: center; gap: 12px; height: 24px; }
  .contact svg { width: 16px; height: 16px; fill: var(--text-grey); }

  .address {
    position: absolute; left: 62px; top: 290px;
    font-style: normal; color: var(--text-grey); font-size: 18px; line-height: 24px;
  }
  .address__web { color: var(--brand-green); font-weight: 700; }
</style>
</head>
<body>
<main class="sheet">
  <section class="card card--back" aria-label="Visitkort, bagside">
    <div class="brand">
      <span class="brand__dot"></span>
      <span class="brand__name">plovnworks</span>
    </div>
  </section>

  <section class="card card--front" aria-label="Visitkort, forside">
    <div class="name-band">
      <p class="name-band__name">Anker Dalsgaard</p>
      <p class="name-band__title">Salgsdirektør</p>
    </div>

    <div class="identity">
      <div class="brand">
        <span class="brand__dot"></span>
        <span class="brand__name">plovnworks</span>
      </div>
      <div class="identity__rule"></div>
      <p class="identity__tagline">idéer der gror</p>
    </div>

    <ul class="contact">
      <li>
        <svg viewBox="0 0 16 16" aria-hidden="true"><path d="M2 6c0-2 3-3 6-3s6 1 6 3l-3 1-1-2H6L5 7 2 6zM4 8h8l1 6H3l1-6zm4 1.5a2 2 0 1 0 0 4 2 2 0 0 0 0-4z"/></svg>
        <span>+45 31 72 40 18</span>
      </li>
      <li>
        <svg viewBox="0 0 16 16" aria-hidden="true"><path d="M2 6c0-2 3-3 6-3s6 1 6 3l-3 1-1-2H6L5 7 2 6zM4 8h8l1 6H3l1-6zm4 1.5a2 2 0 1 0 0 4 2 2 0 0 0 0-4z"/></svg>
        <span>+45 52 60 14 37</span>
      </li>
      <li>
        <svg viewBox="0 0 16 16" aria-hidden="true"><path d="M1 4h14v9H1V4zm1.5 1L8 9.2 13.5 5h-11z"/></svg>
        <span>ad@plovenworks.dk</span>
      </li>
    </ul>

    <address class="address">
      Lindholm Allé 14<br>
      2000 Frederiksberg<br>
      Tlf. +45 31 72 40 18<br>
      <span class="address__web">www.plovenworks.dk</span>
    </address>
  </section>
</main>
</body>
</html>
```